Letterhead Design Project

Looking for letterhead designs for Brastova Mining.

I am looking for a letterhead design in conjunction with a business card design. I have opened contests for both but ask that if you submit a letterhead design you also submit a business card design with a corresponding look/feel.

Brastova Mining is a B2B company that buys and sells large machinery tires within the coal mining industry. The design should the strong, crisp and masculine. I have uploaded the company logo and mock-up of the back of the company's business card.

Color scheme should be grey/green/black

Contact information to include:
Name: Dale Whitford
Title: Managing Director
Phone: 555-231-4097
Address: 1817 Pellam #3 Dallas, TX 75290
Email: Dale@Brastova.example
Updates

Project Deadline Extended
Reason: Looking for a more refined, elegant letterhead than what's been submitted as of yet. Here is a sample of what we're looking for: http://www.plumcrestgallery.example/letterhead-designs/ We will also be increasing the payment.

Industry/Entity Type

Coal Mining

```html
<!DOCTYPE html>
<html lang="en">
<head>
<meta charset="utf-8">
<title>Brastova Mining Letterhead</title>
<link rel="stylesheet" href="https://fonts.googleapis.com/css2?family=Montserrat:wght@500;600&display=swap">
<style>
  :root {
    --backdrop: #2b2b2b;
    --paper: #f4f4f4;
    --paper-shade: #e2e2e2;
    --band: #3a3a3a;
    --brand-green: #5aa02c;
    --text-grey: #555555;
    --watermark: #dcdddc;
  }
  * { margin: 0; padding: 0; box-sizing: border-box; }
  html, body {
    width: 1200px;
    height: 900px;
    overflow: hidden;
    background: var(--backdrop);
    font-family: "Montserrat", sans-serif;
  }
  .canvas {
    position: relative;
    width: 1200px;
    height: 900px;
    display: flex;
    align-items: center;
    justify-content: center;
  }
  .letterhead {
    position: relative;
    width: 660px;
    height: 855px;
    background: linear-gradient(160deg, #fafafa 0%, var(--paper) 45%, var(--paper-shade) 100%);
    display: flex;
    flex-direction: column;
    align-items: center;
  }
  .letterhead__brand {
    margin-top: 46px;
    display: flex;
    align-items: center;
    gap: 8px;
  }
  .brand-mark {
    width: 14px;
    height: 14px;
    background: var(--brand-green);
  }
  .brand-name {
    font-weight: 600;
    font-size: 18px;
    letter-spacing: 2px;
    text-transform: uppercase;
    color: var(--text-grey);
  }
  .letterhead__watermark {
    position: absolute;
    top: 230px;
    left: 50%;
    width: 250px;
    height: 250px;
    transform: translateX(-50%);
    background: var(--watermark);
    opacity: 0.7;
  }
  .letterhead__contact {
    position: absolute;
    bottom: 92px;
    left: 262px;
    display: flex;
    align-items: flex-start;
    gap: 12px;
    font-variant: small-caps;
    font-size: 11px;
    font-weight: 500;
    letter-spacing: 1px;
    line-height: 1.35;
    color: var(--text-grey);
    white-space: nowrap;
  }
  .contact__lines div,
  .contact__address div { white-space: nowrap; }
  .contact__label { color: var(--brand-green); font-weight: 600; }
  .contact__divider {
    width: 1px;
    align-self: stretch;
    background: var(--brand-green);
  }
  .contact__address { font-style: normal; }
  .letterhead__band {
    position: absolute;
    left: 0;
    right: 0;
    bottom: 0;
    height: 62px;
    background: var(--band);
  }
</style>
</head>
<body>
  <main class="canvas">
    <section class="letterhead">
      <header class="letterhead__brand">
        <span class="brand-mark"></span>
        <span class="brand-name">Brastova Mining</span>
      </header>

      <div class="letterhead__watermark" role="img" aria-label="Faint brand decoration"></div>

      <footer class="letterhead__contact">
        <div class="contact__lines">
          <div><span class="contact__label">Phone:</span> 555-231-4097</div>
          <div><span class="contact__label">Email:</span> Dale@Brastova.example</div>
        </div>
        <span class="contact__divider"></span>
        <address class="contact__address">
          <div>1817 Pellam #3 Dallas</div>
          <div>TX 75290</div>
        </address>
      </footer>

      <div class="letterhead__band"></div>
    </section>
  </main>
</body>
</html>
```